Financial Planning firm focused on serving women 55-65 yrs old needs stationary design

We are rebranding our financial planning firm and our target client is a 55-65 yr old women. We need a stationary design to go with our new logo.

Contact Information: Raymond Kessler, MS, CFP President Harlow Wealth Management 4820 Bramblewood Lane, Suite 317 Fernhollow, OR 97412 ray@harlowwealthmgmt.example phone 541-555-0184

```html
<!DOCTYPE html>
<html lang="en">
<head>
<meta charset="utf-8">
<title>Harlow Wealth Management – Business Card</title>
<link href="https://fonts.googleapis.com/css2?family=Montserrat:wght@400;500;600&display=swap" rel="stylesheet">
<style>
  :root {
    --page: #e9ebe8;
    --card-white: #fbfcfb;
    --sage: #a9bfad;
    --sage-light: #c3d3c6;
    --blue: #2f86b7;
    --ink: #3a3f44;
    --rule: #8a9096;
  }
  * { box-sizing: border-box; margin: 0; padding: 0; }
  html, body { width: 1200px; height: 1023px; overflow: hidden; }
  body {
    background: var(--page);
    font-family: "Montserrat", sans-serif;
    display: flex;
    align-items: center;
    justify-content: center;
    gap: 40px;
  }
  .card {
    position: relative;
    width: 540px;
    height: 309px;
    border-radius: 44px 0 44px 0;
    overflow: hidden;
    box-shadow: 0 10px 28px rgba(0,0,0,.18);
  }
  .card svg.wave { position: absolute; inset: 0; }

  /* Front */
  .card-front { background: var(--card-white); }
  .brand {
    position: absolute; left: 34px; top: 46px;
    display: flex; align-items: center; gap: 14px;
  }
  .brand-mark {
    width: 62px; height: 62px; border-radius: 50%;
    background: var(--sage);
  }
  .brand-name {
    color: var(--blue); font-weight: 500;
    font-size: 17px; letter-spacing: .5px; line-height: 1.25;
  }
  .person {
    position: absolute; right: 36px; top: 34px; text-align: right;
  }
  .person-name {
    color: var(--blue); font-size: 17px; font-weight: 500;
    padding-bottom: 4px; border-bottom: 1px solid var(--rule);
  }
  .person-title { color: var(--ink); font-size: 11px; margin-top: 4px; }
  .contact {
    position: absolute; left: 34px; top: 162px;
    border-top: 1px solid var(--rule); padding-top: 10px; width: 240px;
    color: var(--ink); font-size: 11.5px; line-height: 1.5;
  }
  .contact-line { display: flex; align-items: center; gap: 6px; }
  .contact-line svg { width: 10px; height: 10px; fill: var(--blue); }
  .band-text {
    position: absolute; right: 30px; bottom: 26px;
    color: #fff; font-size: 12px; letter-spacing: .4px;
  }

  /* Back */
  .card-back { background: linear-gradient(160deg, var(--sage-light), var(--sage)); }
  .back-brand {
    position: absolute; left: 130px; right: 20px; top: 66px;
    display: flex; flex-direction: column; align-items: center; gap: 18px;
  }
  .back-mark {
    width: 110px; height: 110px; border-radius: 50%;
    background: rgba(255,255,255,.85);
  }
  .back-name {
    color: var(--blue); font-weight: 500; font-size: 22px;
    letter-spacing: .8px; text-align: center; white-space: nowrap;
  }
</style>
</head>
<body>

<section class="card card-front" aria-label="Business card front">
  <svg class="wave" viewBox="0 0 540 309" width="540" height="309" aria-hidden="true">
    <path d="M0,300 C160,306 250,262 320,202 C390,142 455,112 540,104 L540,309 L0,309 Z" fill="var(--sage)"/>
    <path d="M0,292 C160,298 250,254 320,194 C390,134 455,104 540,96" fill="none" stroke="var(--blue)" stroke-width="4"/>
  </svg>

  <div class="brand">
    <div class="brand-mark"></div>
    <div class="brand-name">Harlow Wealth<br>Management</div>
  </div>

  <div class="person">
    <div class="person-name">Raymond Kessler, MS, CFP</div>
    <div class="person-title">President</div>
  </div>

  <div class="contact">
    <div>4820 Bramblewood Lane, Suite 317</div>
    <div>Fernhollow, OR 97412</div>
    <div class="contact-line">
      <svg viewBox="0 0 10 10"><path d="M5,0 L10,5 L8.5,5 L8.5,10 L1.5,10 L1.5,5 L0,5 Z"/></svg>
      ray@harlowwealthmgmt.example
    </div>
    <div class="contact-line">
      <svg viewBox="0 0 10 10"><path d="M1,3 Q1,1 3,1 L7,1 Q9,1 9,3 L7.5,4 L6.5,3 L3.5,3 L2.5,4 Z M2.5,5 L7.5,5 L8.5,9 L1.5,9 Z"/></svg>
      541-555-0184
    </div>
  </div>

  <div class="band-text">Harlow Wealth Management</div>
</section>

<section class="card card-back" aria-label="Business card back">
  <svg class="wave" viewBox="0 0 540 309" width="540" height="309" aria-hidden="true">
    <path d="M0,0 L70,0 C58,120 92,240 210,309 L0,309 Z" fill="var(--card-white)"/>
    <path d="M70,0 C58,120 92,240 210,309" fill="none" stroke="var(--blue)" stroke-width="4"/>
  </svg>
  <div class="back-brand">
    <div class="back-mark"></div>
    <div class="back-name">Harlow Wealth Management</div>
  </div>
</section>

</body>
</html>
```